Brindle Logistics Business Card Design

We are a trucking and warehousing company. We run freight in the US manly from the Pacific NW to TX and back up the the PNW. We also do warehousing where we store, move, and distribute freight. Looking for a clean and modern design of business card. We would like to look rich and elegant. Attached is our logo.

Industry/Entity Type

Trucking Company

Contact Information for Business Card

Looking for a clean and modern design of business card. We would like to look rich and elegant.

Font styles to use
Sans Serif

Colors

Designer to choose colors to be used in the design.

Requirements
Must have
• logo but it should not dominate the card
Should not have
• logo should not dominate the card

```html
<!DOCTYPE html>
<html lang="en">
<head>
<meta charset="utf-8">
<title>Brindle Logistics Business Card</title>
<link rel="stylesheet" href="https://fonts.googleapis.com/css2?family=Exo+2:wght@400;500;600;700&display=swap">
<style>
  :root {
    --stage: #2e2e30;
    --blue-deep: #0d4f9e;
    --blue-mid: #1f78cf;
    --blue-light: #5cb3e6;
    --accent-blue: #1b6fbf;
    --ink: #1c1c1e;
    --paper-top: #ffffff;
    --paper-bottom: #e9e9eb;
    --watermark: #dcdcde;
    --white: #ffffff;
  }
  * { box-sizing: border-box; margin: 0; padding: 0; }
  html, body {
    width: 1200px; height: 900px; overflow: hidden;
    background: var(--stage);
    font-family: "Exo 2", sans-serif;
  }
  .canvas { position: relative; width: 1200px; height: 900px; }
  .card {
    position: absolute; left: 320px;
    width: 560px; height: 320px;
    border-radius: 22px; overflow: hidden;
  }
  .card-front { top: 100px; }
  .card-back { top: 480px; background: linear-gradient(160deg, var(--paper-top) 30%, var(--paper-bottom) 100%); }

  .front-art {
    position: absolute; inset: 0;
    background:
      radial-gradient(ellipse at 20% 80%, var(--blue-deep) 0%, transparent 60%),
      linear-gradient(135deg, var(--blue-mid) 0%, var(--blue-light) 100%);
  }
  .front-name {
    position: absolute; right: 36px; bottom: 62px;
    color: var(--white); font-weight: 500; font-size: 20px;
    letter-spacing: 0.06em; text-transform: uppercase;
  }

  .back-watermark {
    position: absolute; left: 120px; top: 40px; width: 440px; height: 200px;
    background: radial-gradient(ellipse at 60% 45%, var(--watermark) 0%, rgba(220,220,222,0) 70%);
  }
  .back-name {
    position: absolute; right: 30px; top: 44px;
    color: var(--accent-blue); font-weight: 600; font-size: 18px;
    letter-spacing: 0.05em; text-transform: uppercase;
    display: flex; align-items: center; gap: 8px;
  }
  .back-name .dot { width: 12px; height: 12px; border-radius: 50%; background: var(--accent-blue); }

  .person { position: absolute; left: 44px; top: 170px; }
  .person-name { color: var(--ink); font-weight: 700; font-size: 23px; line-height: 1.15; }
  .person-role { color: var(--accent-blue); font-weight: 600; font-size: 18px; }

  .contacts { position: absolute; left: 44px; top: 236px; list-style: none; }
  .contacts li {
    display: flex; align-items: center; gap: 8px;
    color: var(--ink); font-size: 17px; line-height: 24px;
  }
  .contacts svg { width: 15px; height: 15px; flex: none; }

  .address {
    position: absolute; left: 322px; top: 176px;
    color: var(--ink); font-size: 16px; line-height: 21px;
  }
  .address .web { color: var(--accent-blue); font-weight: 700; }
</style>
</head>
<body>
<main class="canvas">
  <section class="card card-front">
    <div class="front-art" role="img" aria-label="Large stylised bird head illustration in blue tones with a yellow beak"></div>
    <p class="front-name">Brindle Logistics, LLC</p>
  </section>

  <section class="card card-back">
    <div class="back-watermark" role="img" aria-label="Faint grey bird head decoration"></div>
    <p class="back-name"><span class="dot"></span>Brindle Logistics, LLC</p>

    <div class="person">
      <p class="person-name">Marcus Ellory</p>
      <p class="person-role">managing director</p>
    </div>

    <ul class="contacts">
      <li>
        <svg viewBox="0 0 16 16"><circle cx="8" cy="8" r="7.5" fill="var(--accent-blue)"/><path d="M5 5.5c0 3 2.5 5.5 5.5 5.5l.8-1.3-1.6-.9-.7.7C8 8.9 7.1 8 6.5 6.9l.7-.7-.9-1.6z" fill="#fff"/></svg>
        555 210 47 83
      </li>
      <li>
        <svg viewBox="0 0 16 16"><circle cx="8" cy="8" r="7.5" fill="var(--accent-blue)"/><rect x="5.5" y="3.5" width="5" height="9" rx="1" fill="none" stroke="#fff" stroke-width="1.2"/></svg>
        555 864 19 02
      </li>
      <li>
        <svg viewBox="0 0 16 16"><circle cx="8" cy="8" r="7.5" fill="var(--accent-blue)"/><rect x="4" y="5" width="8" height="6" fill="none" stroke="#fff" stroke-width="1.1"/><path d="M4 5l4 3.2L12 5" fill="none" stroke="#fff" stroke-width="1.1"/></svg>
        m.ellory@brindlelogistics.com
      </li>
    </ul>

    <address class="address">
      418 Cedar Lane<br>
      Ridgefield, Oregon 97402<br>
      <span class="web">www.brindlelogistics.com</span>
    </address>
  </section>
</main>
</body>
</html>
```